We need a flyer designed for our 4th Annual Brightfield: A Kinfolk Homecoming Harvest Festival that includes the day, time, location, address, and logos. It also needs to include what to expect. The event will be held on Saturday June 14th from 12p-6p at Lantern Commons located at 418 N. Corvella Ave., Pensacola, FL 32507. Please see uploaded files for prior flyers for reference when it comes to information to include. Also I've uploaded pictures from our prior festivals that you may incorporate and logos.

```html
<!DOCTYPE html>
<html lang="en">
<head>
<meta charset="utf-8">
<title>4th Annual Brightfield Festival Flyer</title>
<link rel="stylesheet" href="https://fonts.googleapis.com/css2?family=Anton&family=Oswald:wght@500;600&family=Montserrat:wght@600;700;800;900&display=swap">
<style>
  :root {
    --black: #0b0b0a;
    --yellow: #ffc20e;
    --gold: #f6a91b;
    --orange: #f7931e;
    --red: #f0402b;
    --red-deep: #e63a36;
    --green: #3aa83d;
    --green-deep: #1f7d2b;
    --white: #ffffff;
  }
  * { margin: 0; padding: 0; box-sizing: border-box; }
  html, body { width: 948px; height: 1200px; overflow: hidden; background: #808080; }
  .flyer { position: relative; width: 948px; height: 1200px; background: var(--black); overflow: hidden; font-family: "Montserrat", sans-serif; }
  .backdrop { position: absolute; inset: 0; }
  .edge-band { position: absolute; left: 0; width: 100%; height: 22px; background: var(--yellow); }
  .edge-band.top { top: 0; }
  .edge-band.bottom { bottom: 0; }
  .edge-band::after { content: ""; position: absolute; left: 0; right: 0; height: 6px; background: var(--red); }
  .edge-band.top::after { bottom: 0; }
  .edge-band.bottom::after { top: 0; }

  .presenter { position: absolute; top: 50px; width: 100%; text-align: center; color: var(--yellow); font-weight: 600; font-size: 38px; letter-spacing: -0.5px; }
  .presents { position: absolute; top: 98px; width: 100%; text-align: center; color: var(--green); font-weight: 800; font-size: 26px; letter-spacing: 7px; }

  .title-edition { position: absolute; top: 140px; width: 100%; text-align: center; font-family: "Anton", sans-serif; font-size: 118px; line-height: 1; background: linear-gradient(90deg, var(--green) 38%, var(--yellow) 52%, var(--orange) 64%); -webkit-background-clip: text; background-clip: text; color: transparent; }
  .ribbon { position: absolute; left: 230px; top: 255px; width: 490px; height: 130px; }
  .title-annual { position: absolute; top: 262px; width: 100%; text-align: center; font-family: "Anton", sans-serif; font-size: 78px; line-height: 1; color: var(--black); transform: rotate(0deg); }
  .title-name-top { position: absolute; top: 350px; width: 100%; text-align: center; font-family: "Anton", sans-serif; font-size: 100px; line-height: 1; color: var(--green); letter-spacing: 1px; }
  .title-name-bottom { position: absolute; top: 458px; width: 100%; text-align: center; font-family: "Anton", sans-serif; font-size: 100px; line-height: 1; color: var(--red); letter-spacing: 14px; padding-left: 14px; }

  .date-card { position: absolute; left: 69px; top: 289px; width: 149px; height: 201px; border-radius: 18px; background: var(--red); overflow: hidden; font-family: "Oswald", sans-serif; text-align: center; }
  .date-card .day-block { background: var(--yellow); border-radius: 18px; height: 148px; padding-top: 8px; }
  .date-card .day { font-size: 64px; line-height: 1; color: var(--black); font-weight: 600; }
  .date-card .day sup { font-size: 32px; vertical-align: top; position: relative; top: 2px; }
  .date-card .month { font-size: 50px; line-height: 1; color: var(--red); font-weight: 600; margin-top: 2px; }
  .date-card .weekday { font-size: 34px; line-height: 50px; color: var(--white); font-weight: 600; letter-spacing: -0.5px; }

  .time-card { position: absolute; left: 752px; top: 289px; width: 149px; height: 201px; border-radius: 18px; background: var(--red); font-family: "Oswald", sans-serif; text-align: center; color: var(--white); }
  .time-card .from { margin-top: 16px; font-size: 40px; line-height: 1; color: var(--yellow); font-weight: 500; }
  .time-card .hour { font-size: 58px; line-height: 1; font-weight: 500; }
  .time-card .start { margin-top: 6px; }
  .time-card .joiner { position: absolute; left: 59px; top: 107px; width: 32px; height: 32px; border-radius: 50%; background: var(--green); font-size: 18px; line-height: 32px; color: var(--white); }

  .venue-pill { position: absolute; left: 342px; top: 635px; width: 283px; height: 39px; border-radius: 20px; background: var(--red); color: var(--white); font-weight: 700; font-size: 24px; line-height: 39px; text-align: center; padding-left: 10px; }
  .pin-icon { position: absolute; left: 326px; top: 630px; width: 26px; height: 34px; }
  .venue-address { position: absolute; top: 680px; left: 0; width: 100%; text-align: center; color: var(--white); font-weight: 700; font-size: 20px; line-height: 28px; }

  .photo { position: absolute; }
  .photo-cutout { border-radius: 6px; }
  .photo-dancer { left: 20px; top: 660px; width: 135px; height: 208px; background: linear-gradient(180deg, #2f6b35, #1b1b1b 70%, #2e7d2f); }
  .photo-drummers { left: 738px; top: 636px; width: 210px; height: 273px; background: linear-gradient(180deg, #3a7a3d, #3d4a35 45%, #6b4a2e 80%, #2d2d28); }
  .photo-sign { left: 258px; top: 742px; width: 420px; height: 118px; border-radius: 30px; background: linear-gradient(180deg, #e23b2a 0%, #f3c21a 30%, #35a83a 55%, #dcdcdc 75%, #c9c9c9 100%); }

  .gallery { position: absolute; top: 870px; left: 60px; display: flex; gap: 10px; }
  .gallery .shot { width: 156px; height: 134px; border: 5px solid var(--white); }
  .shot.choir { background: linear-gradient(160deg, #e8e2da, #b77a52 55%, #50403a); }
  .shot.stage { background: linear-gradient(180deg, #d9dfe6, #7c6f66 50%, #3e3a39); }
  .shot.grill { background: linear-gradient(170deg, #4d3f66, #3a3440 50%, #c4622b); }
  .shot.dance { background: linear-gradient(180deg, #d8e0e6, #5b4a7c 55%, #6d7a3e); }
  .shot.street { background: linear-gradient(180deg, #cfd9dd, #d7895a 50%, #8e8a80); }

  .expect-box { position: absolute; left: 54px; top: 1030px; width: 502px; height: 124px; border: 2px solid var(--yellow); border-radius: 8px; padding: 14px 0 0 40px; }
  .expect-box h2 { font-family: "Montserrat", sans-serif; font-weight: 900; font-size: 26px; line-height: 1; color: var(--yellow); letter-spacing: 0.3px; margin-bottom: 8px; }
  .expect-box p { color: var(--white); font-weight: 600; font-size: 14.2px; line-height: 18.5px; }

  .sponsors { position: absolute; left: 606px; top: 1040px; width: 290px; }
  .sponsor { display: flex; align-items: center; gap: 10px; color: var(--white); font-family: "Montserrat", sans-serif; font-weight: 700; font-size: 15px; line-height: 1.15; margin-bottom: 22px; }
  .sponsor .mark { width: 30px; height: 30px; background: var(--gold); flex: none; }
  .sponsor .mark.round { border-radius: 50%; }
</style>
</head>
<body>
<main class="flyer">
  <svg class="backdrop" width="948" height="1200" viewBox="0 0 948 1200" aria-hidden="true">
    <path d="M0 575 L40 582 L75 590 L110 600 L150 598 L185 606 L230 612 L270 604 L320 598 L360 604 L400 597 L450 602 L490 596 L540 590 L580 598 L620 604 L665 610 L700 606 L740 612 L790 618 L840 614 L890 620 L948 618 L948 1200 L0 1200 Z" fill="var(--green)"/>
    <path d="M0 700 L60 690 L130 720 L0 760 Z" fill="var(--green-deep)" opacity="0.35"/>
    <path d="M0 915 Q60 905 120 920 Q200 935 280 918 Q340 905 400 920 Q480 938 560 922 Q640 905 720 918 Q800 930 870 915 Q910 908 948 912 L948 1200 L0 1200 Z" fill="var(--red-deep)"/>
  </svg>

  <div class="edge-band top"></div>

  <p class="presenter">THE HARLOW FAMILY FOUNDATION</p>
  <p class="presents">PRESENTS</p>

  <h1 class="event-title">
    <span class="title-edition">4TH</span>
    <svg class="ribbon" viewBox="0 0 490 130" aria-hidden="true">
      <path d="M0 45 L70 30 L78 112 L30 102 Z" fill="var(--gold)"/>
      <path d="M490 45 L420 30 L412 112 L460 102 Z" fill="var(--gold)"/>
      <path d="M60 30 Q245 -12 430 30 L422 112 Q245 78 68 112 Z" fill="var(--yellow)"/>
    </svg>
    <span class="title-annual">ANNUAL</span>
    <span class="title-name-top">BRIGHT</span>
    <span class="title-name-bottom">FIELD</span>
  </h1>

  <div class="date-card">
    <div class="day-block">
      <div class="day">14<sup>TH</sup></div>
      <div class="month">JUNE</div>
    </div>
    <div class="weekday">SATURDAY</div>
  </div>

  <div class="time-card">
    <div class="from">FROM</div>
    <div class="hour start">12PM</div>
    <div class="joiner">TO</div>
    <div class="hour">6PM</div>
  </div>

  <div class="photo photo-dancer photo-cutout" role="img" aria-label="Photo of a young festival-goer dancing in a festival t-shirt"></div>
  <div class="photo photo-drummers photo-cutout" role="img" aria-label="Photo of two drummers in patterned attire playing hand drums"></div>

  <svg class="pin-icon" viewBox="0 0 26 34" aria-hidden="true">
    <path d="M13 1 C6 1 1 6 1 13 C1 22 13 33 13 33 C13 33 25 22 25 13 C25 6 20 1 13 1 Z" fill="var(--yellow)"/>
    <circle cx="13" cy="13" r="4.5" fill="var(--green-deep)"/>
  </svg>
  <div class="venue-pill">LANTERN COMMONS</div>
  <p class="venue-address">located at 418 N. Corvella Ave., Pensacola,<br>FL 32507.</p>

  <div class="photo photo-sign" role="img" aria-label="Photo of a large festival marquee sign topped with red, yellow and green balloons"></div>

  <div class="gallery">
    <div class="shot choir" role="img" aria-label="Photo of women singing together at a past festival"></div>
    <div class="shot stage" role="img" aria-label="Photo of a performance on the festival stage"></div>
    <div class="shot grill" role="img" aria-label="Photo of food vendors grilling"></div>
    <div class="shot dance" role="img" aria-label="Photo of a youth dance troupe performing"></div>
    <div class="shot street" role="img" aria-label="Photo of families dancing in the street"></div>
  </div>

  <section class="expect-box">
    <h2>WHAT TO EXPECT</h2>
    <p>Live Performances Food Vendors. Art/Course &amp; Play<br>Area African Clothing Vendor Kids Obstacle Spades &amp;<br>Domino Tables Bring Your Own Chairs or Picnic Blankets</p>
  </section>

  <div class="sponsors">
    <div class="sponsor"><span class="mark"></span><span>The Harlow Firm, PLLC</span></div>
    <div class="sponsor"><span class="mark round"></span><span>The Harlow Family Foundation</span></div>
  </div>

  <div class="edge-band bottom"></div>
</main>
</body>
</html>
```